A4 Tri-fold Brochure for Sedation Dentist Specialist Dr. Marlon and Sedation Dentistry.

I would like to create an A4 tri-fold brochure for our Dental Sedation Specialist Dr. Marlon Quade. Please carefully select the most suitable highlights from his bio below.

This brochure has two parts. Highlighting what makes Dr. Marlon Quade unique and trustworthy. Include a picture of him (attached). The second part is about sedation dentistry. All you need to know here: http://www.calmchairhub.example/what-is-calm-chair-treatment

Avoid making it too wordy.

Meet Dr. Rowan Elke Marlon Quade, DDS

Inspired to Become a Dentist:
As a child, Dr. Marlon Quade always felt stressed whenever he had to see a dentist. He knew that he wanted to become a dentist to help put patients completely at ease while they experienced quality dental care.

He is passionate about giving patients the healthy, beautiful smiles they deserve. “I find it fulfilling when I can see my patients’ beautiful smiles and how they can finally appreciate the joy of eating with a healthy set of teeth. However, what I love most about my job is the ability to provide a stress-free and comfortable experience at the dentist’s office, particularly for children, through sedation and general anesthesia.”

Educational Achievements:
Before becoming a dentist, Dr. Marlon Quade earned his undergraduate degree at the University of Northern Albury where he received a Bachelor of Medical Science Honor Specialization degree with distinction in biochemistry. He then completed his Doctor of Dental Surgery degree with honors at the University of Kestrelford. While there, he received the Linus Brandt Medal in his class for outstanding achievement in anesthesia. He then pursued his three-year residency as well as a master’s degree in dental anesthesia at the University of Kestrelford.

So he can provide his patients with the latest in dentistry, Dr. Marlon Quade enjoys pursuing additional knowledge, particularly in the areas of dental anesthesia as well as advanced technologies in dentistry. He is currently part of the Molar Horizons study club and has enrolled in the Core Anchor Short- Training Course. He also serves as a clinical instructor at the Pellvar Clinic at the University of Kestrelford.

Association Memberships:
In addition to his academic credentials, Dr. Marlon Quade is a member of several associations:
The Grand Guild of Oral Practitioners of Varnland (GGOPV)
Dental Continental Union of Dental Sedation (CUDS)
Northern Institute of Dental Sedation (NIDS)
Varnland Dental Council (VDC)
Outside the Practice

When he’s not at the practice, Dr. Marlon Quade enjoys spending time with his wife Greta and their two poodles Pippin and Pepper, who are spoiled rotten! “Greta and I love taking our dogs out on hikes and to the dog park on weekends. I also enjoy a wide range of activities from model building and playing the piano to soccer, gym and archery.” He stays fit by working out at the local Brightstride gym, and he likes to walk in Fernhollow Lake Park and Ashcombe Meadow Park.

Dr. Marlon Quade considers himself to be a kid at heart. He is a big fan of superheroes and animated movies. “I get really excited about any upcoming superhero or Lumawell Studioz movies. Till this day, I still collect superhero toy figures.”

He supports the TinyHearts Trust as well as the Varnland League for the Protection of Companion Creatures (LPCC).

Experience outstanding dental care with our highly skilled dentist. Contact us today to schedule an appointment with Dr. Marlon Quade! He speaks English, Cantonese, and Mandarin.

Target Market(s)

Mothers with young kids.

Industry/Entity Type

Dental

Font styles to use
Sans Serif

Requirements
Should not have
• Prices

```html
<!DOCTYPE html>
<html lang="en">
<head>
<meta charset="utf-8">
<title>Meet Dr. Rowan Elke Marlon Quade, DDS – Tri-fold Brochure</title>
<link href="https://fonts.googleapis.com/css2?family=Open+Sans:ital,wght@0,400;0,600;0,700;1,400;1,600&family=Oswald:wght@500;600&family=Roboto:wght@400;700;900&display=swap" rel="stylesheet">
<style>
  :root{
    --blue:#1a7fd0;
    --blue-light:#2fa6e6;
    --orange:#f26a1b;
    --ink:#3a3a3a;
    --footer:#4a4c4f;
    --page:#ffffff;
    --stage:#cfd1d3;
  }
  *{box-sizing:border-box;margin:0;padding:0}
  html,body{width:1200px;height:1200px;overflow:hidden;background:var(--stage)}
  .brochure{position:absolute;left:30px;top:197px;width:1140px;height:806px;display:flex;background:var(--page);box-shadow:0 10px 30px rgba(0,0,0,.18)}
  .panel{position:relative;width:380px;height:100%;overflow:hidden;background:var(--page)}
  .panel + .panel{border-left:1px solid #e4e4e4}

  /* footer band */
  .footer-band{position:absolute;left:0;right:0;bottom:0;height:46px;background:var(--footer);color:#fff;
    font:600 14px/46px "Open Sans",sans-serif;letter-spacing:1px;text-align:center}

  /* left panel */
  .bio{padding:30px 34px 0 34px;color:var(--ink);font-family:"Open Sans",sans-serif}
  .bio h2{font:italic 600 17px/1.2 "Open Sans",sans-serif;color:var(--blue);margin:0 0 8px}
  .bio p{font-size:10.6px;line-height:1.42;text-align:justify;margin-bottom:10px}
  .bio h2.next{margin-top:14px}
  .bio ul{list-style:none;font-size:10.6px;line-height:1.5}
  .bio li{padding-left:10px;position:relative;margin-bottom:3px}
  .bio li::before{content:"";position:absolute;left:0;top:6px;width:4px;height:4px;border-radius:50%;background:var(--ink)}
  .family-photo{position:absolute;left:0;right:0;bottom:46px;height:220px;
    background:linear-gradient(160deg,#f1ece7 0%,#e4cbb4 45%,#c79a76 75%,#f4f4f4 100%)}
  .family-accent{position:absolute;left:0;bottom:46px;width:100%;height:220px}

  /* middle panel */
  .patient-photo{position:absolute;left:0;top:0;width:100%;height:300px;
    background:linear-gradient(120deg,#f3d7c4 0%,#e8b9a0 35%,#f4f4f2 60%,#dfe8ea 100%)}
  .care-wave{position:absolute;left:0;top:0;width:100%;height:806px}
  .care-copy{position:absolute;left:0;right:0;top:268px;text-align:center;color:#fff}
  .care-copy .big{font:400 44px/1 "Roboto",sans-serif;letter-spacing:.5px}
  .care-copy .mid{font:400 22px/1.2 "Roboto",sans-serif;margin-top:2px}
  .care-copy .small{font:700 16px/1.3 "Roboto",sans-serif}
  .cta{position:absolute;left:62px;top:392px;width:256px;padding:14px 10px;background:var(--orange);
    border:2px solid #fff;border-radius:8px;color:#fff;text-align:center;font:700 15px/1.3 "Roboto",sans-serif}
  .contact{position:absolute;left:44px;top:600px;color:var(--ink);font:13px/1.45 "Open Sans",sans-serif}
  .contact-row{display:flex;gap:10px;margin-bottom:8px;align-items:flex-start}
  .contact-row svg{flex:none;margin-top:3px}
  .contact-strip{position:absolute;left:0;right:0;bottom:0;height:22px;background:var(--footer)}

  /* right panel */
  .doctor-photo{position:absolute;left:0;top:0;width:100%;height:560px;
    background:linear-gradient(180deg,#8d5a3e 0%,#a87457 30%,#1f2a4d 55%,#1a2344 100%)}
  .cover-curve{position:absolute;left:0;top:0;width:100%;height:806px}
  .cover-title{position:absolute;left:30px;right:20px;top:560px}
  .cover-title .meet{font:600 54px/1 "Oswald",sans-serif;color:var(--blue);letter-spacing:1px}
  .cover-title .name{font:500 26px/1.15 "Oswald",sans-serif;color:var(--orange);margin-top:8px;text-transform:uppercase}
  .cover-title .tagline{display:inline-block;margin-top:12px;background:var(--blue);color:#fff;border-radius:16px;
    padding:5px 18px;font:400 21px/1.2 "Open Sans",sans-serif}
</style>
</head>
<body>
<main class="brochure">

  <!-- Panel 1: biography -->
  <section class="panel panel-bio">
    <div class="bio">
      <h2>Educational Achievements</h2>
      <p>Before becoming a dentist, Dr. Marlon Quade earned his undergraduate degree at the University of Northern Albury where he received a Bachelor of Medical Science Honor Specialization degree with distinction in biochemistry. He then completed his Doctor of Dental Surgery degree with honors at the University of Kestrelford. While there, he received the Linus Brandt Medal in his class for outstanding achievement in anesthesia. He then pursued his three-year residency as well as a master’s degree in dental anesthesia at the University of Kestrelford.</p>
      <p>So he can provide his patients with the latest in dentistry, Dr. Marlon Quade enjoys pursuing additional knowledge, particularly in the areas of dental anesthesia as well as advanced technologies in dentistry. He is currently part of the Molar Horizons study club and has enrolled in the Core Anchor Short- Training Course. He also serves as a clinical instructor at the Pellvar Clinic at the University of Kestrelford.</p>
      <h2 class="next">Association Memberships</h2>
      <p>In addition to his academic credentials, Dr. Marlon Quade is a member of several associations:</p>
      <ul>
        <li>The Grand Guild of Oral Practitioners of Varnland (GGOPV)</li>
        <li>Dental Continental Union of Dental Sedation (CUDS)</li>
        <li>Northern Institute of Dental Sedation (NIDS)</li>
        <li>Varnland Dental Council (VDC)</li>
      </ul>
    </div>
    <div class="family-photo" role="img" aria-label="Photo of a smiling family with two young children"></div>
    <svg class="family-accent" viewBox="0 0 380 220" preserveAspectRatio="none" aria-hidden="true">
      <path d="M0 60 L40 20 L40 220 L0 220 Z" fill="#6b6e72"/>
      <path d="M380 150 L300 220 L380 220 Z" fill="#6b6e72"/>
    </svg>
    <div class="footer-band">www.calmwelldental.example</div>
  </section>

  <!-- Panel 2: call to action -->
  <section class="panel panel-care">
    <div class="patient-photo" role="img" aria-label="Photo of a patient smiling during a dental check-up"></div>
    <svg class="care-wave" viewBox="0 0 380 806" preserveAspectRatio="none" aria-hidden="true">
      <defs>
        <linearGradient id="careBlue" x1="0" y1="0" x2="1" y2="1">
          <stop offset="0" stop-color="#2fa6e6"/>
          <stop offset="1" stop-color="#1670c2"/>
        </linearGradient>
      </defs>
      <path d="M0 260 C120 228 260 214 380 240 L380 520 C280 500 150 540 0 500 Z" fill="url(#careBlue)"/>
      <path d="M0 252 C120 220 260 206 380 232 L380 240 C260 214 120 228 0 260 Z" fill="#f26a1b"/>
      <path d="M0 500 C150 540 280 500 380 520 L380 560 C280 530 150 575 0 540 Z" fill="#ffffff"/>
      <path d="M200 533 C280 515 330 516 380 524 L380 530 C330 522 280 521 200 539 Z" fill="#f26a1b"/>
    </svg>
    <div class="care-copy">
      <div class="big">Experience</div>
      <div class="mid">outstanding dental care</div>
      <div class="small">with our highly skilled dentist</div>
    </div>
    <div class="cta">Contact us today to schedule an appointment with Dr. Marlon Quade!</div>
    <div class="contact">
      <div class="contact-row">
        <svg width="12" height="16" viewBox="0 0 12 16"><path d="M6 0a6 6 0 0 0-6 6c0 4.5 6 10 6 10s6-5.5 6-10a6 6 0 0 0-6-6zm0 8.5A2.5 2.5 0 1 1 6 3.5a2.5 2.5 0 0 1 0 5z" fill="#3a3a3a"/></svg>
        <div>Calmwell Dental Group<br>48 Harbor Lantern Road, Suite 12<br>Brookvale, ZX 40211</div>
      </div>
      <div class="contact-row">
        <svg width="12" height="12" viewBox="0 0 12 12"><circle cx="6" cy="6" r="5.5" fill="#3a3a3a"/><path d="M.5 6h11M6 .5c-2.5 3-2.5 8 0 11M6 .5c2.5 3 2.5 8 0 11" stroke="#fff" stroke-width=".8" fill="none"/></svg>
        <div>calmwelldental.example</div>
      </div>
      <div class="contact-row">
        <svg width="12" height="12" viewBox="0 0 12 12"><path d="M2.5 0.5l2 2.5-1.2 1.5c.8 1.7 2.2 3.1 3.9 3.9L8.7 7.2l2.6 2-1.3 2.3C5.5 11.2.8 6.5.3 2z" fill="#3a3a3a"/></svg>
        <div>1-800-555-0142</div>
      </div>
    </div>
    <div class="contact-strip"></div>
  </section>

  <!-- Panel 3: cover -->
  <section class="panel panel-cover">
    <div class="doctor-photo" role="img" aria-label="Portrait of Dr. Marlon Quade in navy scrubs with a stethoscope"></div>
    <svg class="cover-curve" viewBox="0 0 380 806" preserveAspectRatio="none" aria-hidden="true">
      <path d="M0 548 C110 500 260 500 380 560 L380 806 L0 806 Z" fill="#ffffff"/>
      <path d="M0 548 C110 500 260 500 380 560 L380 568 C260 510 110 510 0 556 Z" fill="#f26a1b"/>
    </svg>
    <div class="cover-title">
      <div class="meet">MEET</div>
      <div class="name">Dr. Rowan Elke Marlon Quade, DDS</div>
      <div class="tagline">Inspired to Become a Dentist</div>
    </div>
    <div class="footer-band">www.calmwelldental.example</div>
  </section>

</main>
</body>
</html>
```